Billboard for personal injury chiropractors office

We are a personal injury chiropractor clinic.
I need a Billboard with the company name as the dominating factor. Also a smaller picture or 2 of something creative, like a car accident or an arm in a cast off to the sides.
We Like something Clean and Simple and Eye Catching. Please make the picture Small and Off To The Side. The MAIN FOCUS areas are the… name Varden Chiropractic Clinic
At the top CAR ACCIDENT INJURY?
AND at the bottom our number 418-27-FLEXA.
Dr.Milo R. Varden in bold somewhere with the word chiropractor under the doctors name in a text.

Im open to red lettering on white backgrounds, red on yellow backgrounds and I'm also open to reds blues white and yellow. I'd prefer yellow if used be across the bottom.

I am uploading a very rough draft of what we are after along with a screenshot of the tv commercial showing the yellow

DO NOT USE THE LOGO ON THE COMMERCIAL. I JUST WANT THE NAME TYPED LIKE ON SAMPLE BILLBOARD.

Industry/Entity Type

Chiropractic

Colors
0054AA
0677BA
7BADD7
CADEEF
E8F1F8
FFF300
FFF600
FEFA6F
FFFEC7
FFFEE8
EB3D1F
EC4F4E
F09395
F8D3D4
FCEDEE

Requirements
Must have
• Eye catching ,bold

```html
<!DOCTYPE html>
<html lang="en">
<head>
<meta charset="utf-8">
<title>Varden Chiropractic Clinic – Billboard</title>
<link rel="stylesheet" href="https://fonts.googleapis.com/css2?family=Oswald:wght@500;600&family=Montserrat:wght@800&display=swap">
<style>
  :root {
    --stage: #111111;
    --board-white: #ffffff;
    --accent-red: #e3000f;
    --accent-red-light: #ec4f4e;
    --band-cyan: #00abe6;
    --band-cyan-dark: #0677ba;
    --shirt-blue: #0054aa;
    --shirt-blue-light: #2a6fc0;
    --car-silver: #b9c6d6;
    --car-silver-dark: #6f7c8c;
    --ink: #1a1a1a;
    --link-blue: #0677ba;
    --call-yellow: #fff300;
    --text-white: #ffffff;
  }
  html, body {
    margin: 0;
    padding: 0;
    width: 1085px;
    height: 1200px;
    overflow: hidden;
    background: var(--stage);
  }
  .canvas {
    position: relative;
    width: 1085px;
    height: 1200px;
  }
  .billboard {
    position: absolute;
    left: 42px;
    top: 454px;
    width: 1000px;
    height: 291px;
    display: block;
  }
  .board-bg { fill: var(--board-white); }
  .headline-band { fill: url(#redGrad); }
  .name-band { fill: url(#cyanGrad); }
  .call-band { fill: var(--accent-red); }
  .headline, .clinic-name {
    font-family: "Oswald", "Arial Narrow", sans-serif;
    font-weight: 500;
    fill: var(--text-white);
  }
  .doctor {
    font-family: "Oswald", "Arial Narrow", sans-serif;
    font-weight: 600;
    fill: var(--ink);
  }
  .doctor .role { fill: var(--link-blue); font-weight: 500; }
  .call-line {
    font-family: "Montserrat", "Arial Black", sans-serif;
    font-weight: 800;
    fill: var(--call-yellow);
  }
</style>
</head>
<body>
<main class="canvas">
  <svg class="billboard" viewBox="0 0 1000 291" aria-label="Varden Chiropractic Clinic billboard">
    <defs>
      <linearGradient id="redGrad" x1="0" y1="0" x2="0" y2="1">
        <stop offset="0" stop-color="#f0443a"/>
        <stop offset="0.45" stop-color="#e3000f"/>
        <stop offset="1" stop-color="#d0000c"/>
      </linearGradient>
      <linearGradient id="cyanGrad" x1="0" y1="0" x2="1" y2="0">
        <stop offset="0" stop-color="#00b3ec"/>
        <stop offset="1" stop-color="#00a3dd"/>
      </linearGradient>
      <linearGradient id="shirtGrad" x1="0" y1="0" x2="1" y2="0">
        <stop offset="0" stop-color="var(--shirt-blue)"/>
        <stop offset="0.7" stop-color="var(--shirt-blue-light)"/>
        <stop offset="1" stop-color="#e9d2bf"/>
      </linearGradient>
      <linearGradient id="carGrad" x1="0" y1="0" x2="1" y2="1">
        <stop offset="0" stop-color="#e8edf3"/>
        <stop offset="0.5" stop-color="var(--car-silver)"/>
        <stop offset="1" stop-color="var(--car-silver-dark)"/>
      </linearGradient>
    </defs>

    <rect class="board-bg" x="0" y="0" width="1000" height="291"/>

    <rect class="photo-arm-sling" x="0" y="0" width="300" height="222" fill="url(#shirtGrad)"
          role="img" aria-label="Photo: person in a blue shirt with an arm in a white cast and sling"/>
    <rect class="photo-damaged-car" x="745" y="0" width="255" height="222" fill="url(#carGrad)"
          role="img" aria-label="Photo: silver car with a crushed front end after a collision"/>

    <polygon class="headline-band" points="198,0 813,0 768,86 237,86"/>
    <text class="headline" x="503" y="73" text-anchor="middle" font-size="66" textLength="518" lengthAdjust="spacingAndGlyphs">CAR ACCIDENT INJURY?</text>

    <polygon class="name-band" points="160,87 963,87 981,159 146,159"/>
    <text class="clinic-name" x="502" y="153" text-anchor="middle" font-size="72" textLength="640" lengthAdjust="spacingAndGlyphs">VARDEN CHIROPRACTIC CLINIC</text>

    <text class="doctor" x="320" y="210" font-size="34" textLength="404" lengthAdjust="spacingAndGlyphs">Dr.Milo R. Varden <tspan class="role">(chiropractor)</tspan></text>

    <rect class="call-band" x="0" y="222" width="1000" height="69"/>
    <text class="call-line" x="500" y="276" text-anchor="middle" font-size="54" textLength="712" lengthAdjust="spacingAndGlyphs">Call Now 418-27-FLEXA</text>
  </svg>
</main>
</body>
</html>
```